Modern, crisp, funky web 2.0 site required for childrens holiday programmes

We want a new "Wow" website. Please help this become a reality.

Playvorn is a provider of childrens holiday programmes aimed primary at children 5yrs to 12 yrs. You can view our current site at www.playvorn.co.nz

This website is a primarily a booking portal. Parents typically come to the website to register and book for courses after having seen them in a booklet. However we are changing the marketing approach and are now trying to attract parents directly to the website. Therefore we want the website to be very graphically appealing, very easy to browse and navigate and must be easy to register and book.

The front end is what is being re-designed. The new front end MUST be compatible with the existing back-end system and processes and the back-end should not need to be changed at all. People lodging a tender must familiarise themselves with the existing site and ensure that the new front end will be fully compatible.

The site must be PHP

This tender will not include a re-design of the logo. Please use the current logo which is attached with this document.

Everything else is up for re-design. The site needs a new, clean, crisp modern design. (See Likes and Dislikes).

Some yellow must be used somewhere within the colour scheme to be in keeping with the brand colours. However no yellow background please.

We currently operate in 2 main regions: Auckland and Palmerston North. However we will be adding new regions soon. The website should make it easy for users to find courses in their region easily.

We also offer term time activities – the site needs another area for that. Perhaps emulated as another “region”.

Beyond that courses are offered across a range of activities. Ideally the website would organise courses logically so that users can find what they are looking for easily.

However, if possible it would be good for the user to be able to browse by area. For example within Auckland there would be North Shore, Central, West, East and South. Within each area a range of course are available – e.g. Skateboarding, Surfing etc. However we don’t want this to be the primary design goal. This is more a “could have” than a “must have”

Once the user has found the course they want the site needs to have a course identification button / tab / box e.g. Tennis. Once the user has clicked through all the details pertaining to the tennis courses on offer should be presented. People are used to searching the existing website in this manner.

When clients click through from the course they have chosen to book the GREEN box that’s say “More Info” needs to be changed to say Book Now

Needs to the ability to have photos displayed on each page next to course descriptions or a panel of photos showing the children doing the activity displayed on that page.

Needs the ability to select the “Pick up locations” To show up in the booking form and class attendance sheet e.g. 7.45am/4.45pm: Ferndip Burgerhut Carpark. In front of Burgerhut by the shopping trundler bay.
8.10am/4.10pm: Tallow Cove Reserve, Brindle Hill Road, Orrisdale in the car park in form of the tennis courts

Needs to have Course options above the line (at the top of the page)

Needs to have a description of Playvorn below the line (at the bottom of the page)

You can provide stock images but they must be New Zealand activities (i.e. not American Football) and pre-approved by us. Alternatively we can supply some images.

What adjectives should best describe your website design?
Clean, modern, professional, vibrant, both kid and adult appealing, fun, interesting

What content must be included in the website design?

• Home page
• Contact us
• Testimonials
• Terms and conditions
• New customer sign or log in
• My account or existing client log in
• Chatterbook button,
• Sign up to the newsletter (postwren)
• Refer a friend option – where they input a friend’s contact details, we then send them a one-off email “from” the friend with a HTML email describing our website. Content of the email must be able to be modified easily later (by a programmer).
• “Become a course provider” enquiry tab. This could be a simple form which emails details through.
• Have “View latest booklet” tab which downloads a PDF of the booklet after submitting the users email address onto our PostWren mailing list (must offer postwren integration).
• Must support Zorvex analytics data collection
Updates

Reason: I have not really seen anything that greatly excites me. I am concerned we re not getting the level of design work in as committed to on the starting up stage we only have 18 designs (Many from the same designer and repeats) I was expecting closer to 50. Please can you assist and advise as to how to improve the results thanks Gwen

Target Market(s)

Parents, both working and stay at home, children aged 5-15 years of age with middle – high income.

Industry/Entity Type

Marketing

Requirements
Must have
• The site must be easy to use and navigate.

Users need to be able to navigate with the minimal number of clicks as the site is used by busy mums with no patience!

Users should be able to find exactly what they want with absolute ease.

Needs to be appealing to children aged 5 – 12 years old as well as parents of children within that age range.

Needs to have lots of images of children doing the activities offered. Should NOT have cartoon images!

Must be able to written in PHP – this is to enable it to be compatible with the existing back-end.

Likes:

Big Icons
Clean, crisp design
Vivid, striking in appearance
Uncluttered
Easy to navigate
Social Media integration
Modern
Not much ‘below the line’
Thematically consistent
Easily modifiable pictures and content
Like real images
Search bar would be good if effective ONLY

What colours do you want to see in your website design?
The Yellow in the logo BUT NOT as the background, purple as in the balls etc on logo, white for clean and simple easy to read, black for writing and other areas for details ie boarders etc.
Should not have
• Dislikes:

Cartoon images – must be real images.
Moving, floating in and out and spinning pictures text or photos
Clutter
Underlining
Intentionally misspelt words and typos
Content ‘below the line’ on the Home page
Backgrounds ending before the edge of the screen

What colours do you NOT want to see in your website design?
Browns, pink, pastel colours, mustard, pale yellow, and not a confusion of colours – must be themed and consistent.

```html
<!DOCTYPE html>
<html lang="en">
<head>
<meta charset="utf-8">
<title>Playvorn – A World of Fun Activities</title>
<link rel="stylesheet" href="https://fonts.googleapis.com/css2?family=Arimo:ital,wght@0,400;0,700;1,400&family=Roboto+Condensed:wght@400;700&display=swap">
<style>
:root{
  --white:#ffffff;
  --ink:#2b1f17;
  --brand-yellow:#f1b800;
  --hero-yellow-light:#f7cf1c;
  --hero-yellow-deep:#eab000;
  --form-brown:#2f241d;
  --form-border:#4a3a2f;
  --green-dark:#0b5e22;
  --green:#13862f;
  --green-light:#1b9a38;
  --aqua:#4fb0c4;
  --aqua-text:#173b4a;
  --quote-grey:#dedcda;
  --footer-brown:#3a2a1f;
  --footer-dark:#2a1d14;
  --footer-text:#8d6f58;
  --footer-input:#6b4e38;
  --required:#f1b800;
}
*{box-sizing:border-box;margin:0;padding:0}
html,body{width:1156px;height:1200px;overflow:hidden;background:var(--white)}
body{font-family:"Arimo",Arial,sans-serif;color:var(--ink);position:relative}
.abs{position:absolute}

/* header */
.account-link{left:849px;top:0;width:184px;height:28px;background:var(--green);color:var(--white);
  font-family:"Roboto Condensed",sans-serif;font-size:17px;line-height:28px;text-align:center;border-radius:0 0 3px 3px}
.brand{left:132px;top:26px;display:flex;align-items:center;gap:8px}
.brand-dot{width:22px;height:22px;border-radius:50%;background:var(--brand-yellow)}
.brand-name{font-size:40px;font-weight:700;color:var(--ink);letter-spacing:-1px}
.brand-tag{left:162px;top:82px;font-size:10px;color:var(--ink);letter-spacing:.2px}
.main-nav{left:454px;top:56px;display:flex;gap:0;align-items:center}
.main-nav a{font-size:18px;color:var(--ink);text-decoration:none;height:30px;line-height:30px;padding:0 14px;margin-right:7px}
.main-nav a.current{background:var(--form-brown);color:var(--white);border-radius:2px;padding:0 15px;margin-right:3px}

/* hero */
.hero{left:0;top:120px;width:1156px;height:427px;
  background:radial-gradient(ellipse at 55% 40%,var(--hero-yellow-light) 0%,var(--hero-yellow-deep) 75%)}
.hero-photo{left:160px;top:107px;width:818px;height:346px;
  background:linear-gradient(180deg,#f0c24a 0%,#e99a6a 45%,#d9453a 80%,#e7a0b6 100%);border-radius:140px 140px 0 0;opacity:.85}

/* registration form */
.register-panel{left:120px;top:453px;width:914px;height:185px;background:var(--form-brown);border-radius:3px}
.field-label{font-size:12.5px;color:var(--white);text-align:right;width:110px}
.field-label .req{color:var(--required);font-size:10px;vertical-align:top}
.field{height:26px;background:var(--white);border-radius:2px;font-size:11px;color:#555;padding:0 0 0 23px;line-height:26px}
.field.large{font-size:13px}
.select-tick{position:absolute;right:8px;top:6px;width:14px;height:14px}
.check-line{font-size:11px;color:var(--white)}
.check-line .hl{color:var(--brand-yellow)}
.checkbox{width:12px;height:12px;background:#ddd;border-radius:2px}
.register-btn{left:893px;top:584px;width:121px;height:38px;background:var(--brand-yellow);border-radius:3px;
  font-size:19px;font-weight:700;color:var(--ink);text-align:center;line-height:38px}

/* regions */
.region-menu{left:120px;top:648px;width:239px;height:141px;background:var(--green)}
.region{position:absolute;left:0;width:239px;font-size:18px;font-weight:700;color:var(--white);padding-left:17px}
.region.active{background:var(--green-dark)}
.region svg{position:absolute;right:24px}
.region-sep{position:absolute;left:17px;width:205px;height:1px;background:rgba(255,255,255,.25)}

/* courses */
.course-panel{left:383px;top:646px;width:650px;height:264px;border-radius:3px;
  background:linear-gradient(135deg,var(--green-dark) 0%,var(--green-light) 50%,var(--green-dark) 100%)}
.course-pointer{left:374px;top:654px}
.course-list{list-style:none;font-size:13px;color:var(--white);line-height:20.5px}
.col-divider{width:1px;height:256px;background:rgba(0,0,0,.25);top:650px}

/* help box */
.help-box{left:121px;top:798px;width:238px;height:254px;background:var(--aqua)}
.help-inner{left:129px;top:806px;width:222px;height:238px;border:1px solid rgba(255,255,255,.35)}
.help-text{left:140px;top:816px;width:210px;font-size:13.5px;line-height:18px;color:var(--white)}
.region-name{font-size:20px;color:var(--aqua-text)}
.region-phone{font-size:13.5px;color:var(--white)}
.mail-bar{left:135px;top:1012px;width:209px;height:25px;background:var(--brand-yellow);font-size:13.5px;color:var(--white);line-height:25px;padding-left:39px}
.mail-bar svg{position:absolute;left:8px;top:6px}

/* testimonial */
.rule{left:396px;top:919px;width:637px;height:1px;background:#ddd}
.section-title{left:396px;top:930px;font-size:20px;color:var(--ink)}
.author{left:396px;top:988px;width:98px;text-align:right}
.author-name{font-size:18px}
.author-role{font-size:10px;font-style:italic;color:#888}
.quote{left:516px;top:965px;width:517px;height:87px;background:var(--quote-grey);font-size:12px;line-height:16px;color:#444;padding:13px 16px}
.quote-tip{left:507px;top:998px}

/* footer */
.footer{left:0;top:1090px;width:1156px;height:83px;background:var(--footer-brown)}
.footer-base{left:0;top:1173px;width:1156px;height:27px;background:var(--footer-dark)}
.footer-text{font-family:"Roboto Condensed",sans-serif;color:var(--footer-text)}
.news-label{left:160px;top:1112px;width:86px;font-size:17px;line-height:21px;text-align:right}
.news-input{left:278px;top:1116px;width:168px;height:31px;background:var(--footer-input);font-size:16px;color:#a8866c;padding-left:8px;line-height:31px}
.follow{left:494px;top:1122px;font-size:17px}
.social{width:27px;height:27px;background:var(--footer-input);border-radius:3px;top:1118px}
.company{left:770px;top:1098px;font-size:13px;color:var(--footer-text);line-height:21px}
.company strong{font-family:"Roboto Condensed",sans-serif;font-size:17px}
.copyright{left:122px;top:1182px;font-size:11.5px;color:#5c4536}
</style>
</head>
<body>

<header>
  <a class="abs account-link">My Account &nbsp;/ Register</a>
  <div class="abs brand"><span class="brand-dot"></span><span class="brand-name">Playvorn</span></div>
  <div class="abs brand-tag">A WORLD OF FUN ACTIVITIES</div>
  <nav class="abs main-nav">
    <a class="current">Home</a><a>Courses</a><a>Testimonials</a><a>Contact</a><a>Terms &amp; Conditions</a>
  </nav>
</header>

<section class="abs hero"></section>
<div class="abs hero-photo" role="img" aria-label="Photo of four smiling children resting their chins on their hands"></div>

<form class="abs register-panel" aria-label="Register"></form>
<!-- column 1 -->
<div class="abs field-label" style="left:79px;top:476px"><span class="req">*</span>Title:</div>
<div class="abs field" style="left:205px;top:470px;width:72px">Mr<svg class="select-tick" viewBox="0 0 14 14"><circle cx="7" cy="7" r="7" fill="#2fa64a"/><path d="M4 7l2 2 4-4" stroke="#fff" stroke-width="2" fill="none"/></svg></div>
<div class="abs field-label" style="left:79px;top:518px"><span class="req">*</span>Name:</div>
<div class="abs field" style="left:205px;top:512px;width:158px">Name</div>
<div class="abs field-label" style="left:79px;top:562px"><span class="req">*</span>Surname:</div>
<div class="abs field large" style="left:205px;top:556px;width:158px">Surname</div>
<div class="abs field-label" style="left:79px;top:604px"><span class="req">*</span>E-mail:</div>
<div class="abs field large" style="left:205px;top:598px;width:158px">E-mail</div>
<!-- column 2 -->
<div class="abs field-label" style="left:326px;top:478px">Adress:</div>
<div class="abs field" style="left:453px;top:469px;width:158px;height:71px">Adress</div>
<div class="abs field-label" style="left:326px;top:562px">City:</div>
<div class="abs field" style="left:453px;top:556px;width:158px">Select City<svg class="select-tick" viewBox="0 0 14 14"><circle cx="7" cy="7" r="7" fill="#2fa64a"/><path d="M4 6l3 3 3-3" stroke="#fff" stroke-width="2" fill="none"/></svg></div>
<div class="abs field-label" style="left:326px;top:604px">Suburb:</div>
<div class="abs field" style="left:453px;top:598px;width:158px">Please Select<svg class="select-tick" viewBox="0 0 14 14"><circle cx="7" cy="7" r="7" fill="#2fa64a"/><path d="M4 6l3 3 3-3" stroke="#fff" stroke-width="2" fill="none"/></svg></div>
<!-- column 3 -->
<div class="abs field-label" style="left:587px;top:476px">PIN:</div>
<div class="abs field" style="left:715px;top:470px;width:157px">Adress</div>
<div class="abs field-label" style="left:587px;top:518px"><span class="req">*</span>Phone:</div>
<div class="abs field" style="left:715px;top:512px;width:157px">Phone</div>
<div class="abs field-label" style="left:587px;top:562px"><span class="req">*</span>Password:</div>
<div class="abs field" style="left:715px;top:556px;width:157px">Password</div>
<div class="abs field-label" style="left:587px;top:604px"><span class="req">*</span>Confirm:</div>
<div class="abs field" style="left:715px;top:598px;width:157px">Confirm Password</div>
<!-- column 4 -->
<div class="abs checkbox" style="left:892px;top:478px"></div>
<div class="abs check-line" style="left:918px;top:469px;line-height:16px">I agree to the<br><span class="hl">Terms and Conditions</span></div>
<div class="abs checkbox" style="left:892px;top:515px"></div>
<div class="abs check-line" style="left:914px;top:514px">Subscribe to newsleter</div>
<div class="abs check-line" style="left:892px;top:540px"><span class="hl">★</span> Required fields</div>
<div class="abs register-btn">Register</div>

<nav class="abs region-menu">
  <div class="region active" style="top:0;height:48px;line-height:48px">Auckland<svg style="top:16px" width="16" height="16" viewBox="0 0 16 16"><circle cx="8" cy="8" r="8" fill="#f1b800"/><path d="M5 8h5M8 5l3 3-3 3" stroke="#0b5e22" stroke-width="2" fill="none"/></svg></div>
  <div class="region" style="top:48px;height:45px;line-height:45px">Palmerston<svg style="top:14px" width="16" height="16" viewBox="0 0 16 16"><circle cx="8" cy="8" r="8" fill="#f1b800"/><path d="M5 8h5M8 5l3 3-3 3" stroke="#13862f" stroke-width="2" fill="none"/></svg></div>
  <div class="region-sep" style="top:93px"></div>
  <div class="region" style="top:93px;height:48px;line-height:48px">Mid Term Activities<svg style="top:17px" width="16" height="16" viewBox="0 0 16 16"><circle cx="8" cy="8" r="8" fill="#f1b800"/><path d="M5 8h5M8 5l3 3-3 3" stroke="#13862f" stroke-width="2" fill="none"/></svg></div>
</nav>

<section class="abs course-panel" aria-label="Courses"></section>
<svg class="abs course-pointer" width="10" height="20" viewBox="0 0 10 20"><path d="M10 0L0 10l10 10z" fill="#0b5e22"/></svg>
<div class="abs col-divider" style="left:593px"></div>
<div class="abs col-divider" style="left:821px"></div>
<ul class="abs course-list" style="left:404px;top:661px">
  <li>Acting</li><li>All Week/Daily Action Combo</li><li>All Week/Daily Kids Club</li><li>Animal Care</li><li>Archery</li><li>Art</li><li>Bikes</li><li>Cooking</li><li>Dance</li><li>Drama</li><li>Snow Camps</li>
</ul>
<ul class="abs course-list" style="left:622px;top:661px">
  <li>Farm Camps</li><li>Fencing</li><li>Futsal: Indoor Soccer</li><li>Golf</li><li>Gymnastics</li><li>Horseriding Oakvale Riding Sch</li><li>Horseriding Fernbrook Ridge</li><li>Horseriding Kowhai Rides</li><li>Jewellery</li><li>Brick Corner</li><li>Skateboarding</li>
</ul>
<ul class="abs course-list" style="left:847px;top:661px">
  <li>Farm Camps</li><li>Fencing</li><li>Futsal: Indoor Soccer</li><li>Golf</li><li>Gymnastics</li><li>Horseriding Oakvale Riding Sch</li><li>Horseriding Fernbrook Ridge</li><li>Horseriding Kowhai Rides</li><li>Jewellery</li><li>Brick Corner</li><li>Skateboarding</li>
</ul>

<aside class="abs help-box"></aside>
<div class="abs help-inner"></div>
<div class="abs help-text">
  <p>If you can't find a programme you are looking for please let us know, and we'll see if we can arrange it for you</p>
  <p class="region-name" style="margin-top:14px">Auckland</p>
  <p class="region-phone" style="margin-top:2px">555 0142</p>
  <p class="region-name" style="margin-top:2px;font-size:18px">Palmerston North</p>
  <p class="region-phone" style="margin-top:2px">555 0187</p>
</div>
<div class="abs mail-bar"><svg width="20" height="13" viewBox="0 0 20 13"><rect width="20" height="13" fill="#1e4a8a"/><path d="M0 0l10 7 10-7" stroke="#f1b800" stroke-width="2" fill="none"/></svg>enquiries@playvorn.co.nz</div>

<div class="abs rule"></div>
<h2 class="abs section-title" style="font-weight:400">Testimonial</h2>
<div class="abs author"><div class="author-name">James</div><div class="author-role">Lorem Ipsum</div></div>
<svg class="abs quote-tip" width="10" height="20" viewBox="0 0 10 20"><path d="M10 0L0 10l10 10z" fill="#dedcda"/></svg>
<blockquote class="abs quote">My Jack has just finished Pee Wee Tennis and he had a great time. I thought he had no hand-eye coordination but the Coach 'found' it. Playvorn courses never cease to amaze me-they always seen to find the "able-ities" in our children thet we as parents cannot. It must be the fun group learning environments that they're in. Thank You</blockquote>

<footer class="abs footer"></footer>
<div class="abs footer-base"></div>
<div class="abs footer-text news-label">Sign up for Newsletter</div>
<div class="abs footer-text news-input">Email Adress</div>
<div class="abs footer-text follow">Follow Us :</div>
<div class="abs social" style="left:579px" role="img" aria-label="Chatterbook"></div>
<div class="abs social" style="left:626px" role="img" aria-label="Chirpline"></div>
<div class="abs company"><strong>Playvorn Ltd</strong><br>Postal: P O Box 402, Kestrel Bay, Auckland 0790<br>Office: Marlowe Road, Auckland 0790</div>
<div class="abs copyright">All content copyright their owners. Pixelmoor copyright 2012 Quillbyte, LLC.</div>

</body>
</html>
```